VENTIX Business Card

VENTIX (www.ventixpools.example) is a veteran in the swimming pool maintenance and repair business..we have served our clients for 15 years and have a research chemist, an electrician, a plumber and a pool building contractor (in part) on staff...We want to provide a business card that has a dual purpose, that people want to keep around, that leaves people speechless in the sense that they understand the mission of and the experience level of the TEAM at VENTIX.

Target Market(s)

persons who enjoy swimming and make it a priority to swim

Industry/Entity Type

Building

Font styles to use
Serif
Sans Serif

Colors
85acd3
3176b5
95b6d8
3276b5
0355a3
0555a3
0255a3
0455a3
85abd2

Requirements
Must have
• name, title, address, email, text
Nice to have
• a die cut shape
Should not have
• cartoons, pictures of pools

```html
<!DOCTYPE html>
<html lang="en">
<head>
<meta charset="utf-8">
<title>VENTIX Business Card</title>
<link rel="stylesheet" href="https://fonts.googleapis.com/css2?family=Montserrat:wght@300;400;600&display=swap">
<style>
  :root {
    --card-blue: #2280b2;
    --paper: #ffffff;
    --backdrop: #f2f2f2;
    --ink-light: #ffffff;
  }
  * { box-sizing: border-box; margin: 0; padding: 0; }
  html, body {
    width: 1200px; height: 800px; overflow: hidden;
    background: var(--backdrop);
    font-family: "Montserrat", Arial, sans-serif;
  }
  .canvas { position: relative; width: 1200px; height: 800px; }
  .card {
    position: absolute; top: 257px;
    width: 500px; height: 286px;
    background: var(--card-blue);
    color: var(--ink-light);
    overflow: hidden;
  }
  .card--contact { left: 70px; }
  .card--brand { left: 630px; }

  .brand {
    position: absolute;
    display: flex; align-items: center;
    color: var(--ink-light);
    font-weight: 600; letter-spacing: 0.04em; line-height: 1;
    white-space: nowrap;
  }
  .brand__dot {
    flex: none; border-radius: 50%;
    background: var(--paper);
  }

  /* contact side */
  .card--contact .brand { left: 118px; top: 62px; font-size: 30px; gap: 12px; }
  .card--contact .brand__dot { width: 26px; height: 26px; }
  .person__name {
    position: absolute; left: 118px; top: 124px;
    font-size: 30px; font-weight: 300; letter-spacing: 0.01em; line-height: 1.2;
  }
  .person__title {
    position: absolute; left: 188px; top: 168px;
    font-size: 21px; font-weight: 300; line-height: 1.2;
  }
  .divider {
    position: absolute; left: 26px; right: 26px; top: 217px;
    border-top: 1.5px dashed var(--ink-light);
  }
  .contact {
    position: absolute; top: 228px;
    font-size: 10px; font-weight: 300; line-height: 1.45;
  }
  .contact--reach { left: 30px; }
  .contact--address { left: 300px; display: flex; gap: 6px; line-height: 1.3; }
  .contact--address ul { list-style: none; }

  /* brand side */
  .card--brand .brand {
    left: 0; right: 0; top: 92px; justify-content: center;
    font-size: 46px; gap: 16px;
  }
  .card--brand .brand__dot { width: 38px; height: 38px; }
  .website {
    position: absolute; left: 0; right: 0; top: 218px;
    text-align: center; font-size: 22px; font-weight: 300; letter-spacing: 0.03em;
  }
</style>
</head>
<body>
<main class="canvas">
  <section class="card card--contact" aria-label="Business card, contact side">
    <div class="brand"><span class="brand__dot"></span><span class="brand__name">VENTIX</span></div>
    <h1 class="person__name">Name Here</h1>
    <p class="person__title">Title Here</p>
    <div class="divider"></div>
    <p class="contact contact--reach">Tel: 555-014-2290<br>Email: hello@ventixpools.example</p>
    <div class="contact contact--address">
      <span>Address:</span>
      <ul>
        <li>240 HARBOR AVE</li>
        <li>PO BOX 4410</li>
        <li>TACOMA WA 98402</li>
        <li>USA</li>
      </ul>
    </div>
  </section>

  <section class="card card--brand" aria-label="Business card, brand side">
    <div class="brand"><span class="brand__dot"></span><span class="brand__name">VENTIX</span></div>
    <p class="website">www.ventixpools.example</p>
  </section>
</main>
</body>
</html>
```